Verpackungen für ein CBD Öl
Zielgruppe
Wir bringen ein neues CBD Öl auf den Markt. Unsere Zielgruppe sind Männer und Frauen ab 18 Jahren die natürliche Produkte den 'Chemischen' bevorzugen.
Aufgabenstellung
Es soll bitte eine Faltschachteln für ein CBD Öl designt werden. Die Stanzvorlage habe ich hochgeladen. Als Name des CBD Öls bitte erstmal 'XX' nehmen. Wir werden den Namen zu einem späteren Zeitpunkt nennen. Wichtig ist, dass das Design modern und eher 'edel' aussieht.
Die Pflichttexte, Namen, Barcode etc. können zu einem späteren Zeitpunkt hinzugefügt werden.
Es geht erstmal nur um ein schönes Design :-)

```html
<!DOCTYPE html>
<html lang="de">
<head>
<meta charset="utf-8">
<title>CBD Öl – Faltschachtel</title>
<link rel="stylesheet" href="https://fonts.googleapis.com/css2?family=Montserrat:wght@300;400;600&display=swap">
<style>
  :root {
    --paper: #ffffff;
    --box-green: #3b4733;
    --band-green: #263316;
    --leaf-green: #4a5736;
    --leaf-light: #56653d;
    --gold: #e8d06c;
    --outline: #0d1208;
    --white: #ffffff;
  }
  html, body {
    margin: 0;
    padding: 0;
    width: 839px;
    height: 1200px;
    overflow: hidden;
    background: var(--paper);
  }
  .dieline-canvas { display: block; width: 839px; height: 1200px; }
  .box-surface { fill: var(--box-green); }
  .box-outline { fill: none; stroke: var(--outline); stroke-width: 3; }
  .info-band { fill: var(--band-green); }
  .badge-ring { fill: var(--gold); }
  .badge-core { fill: var(--band-green); }
  .badge-arc { fill: none; stroke: var(--gold); stroke-width: 3; }
  .rule-line { stroke: var(--gold); stroke-width: 3; }
  .brand-top { font-family: 'Montserrat', sans-serif; font-weight: 400; font-size: 36px; fill: var(--white); }
  .badge-name { font-family: 'Montserrat', sans-serif; font-weight: 300; font-size: 52px; fill: var(--gold); }
  .product-title { font-family: 'Montserrat', sans-serif; font-weight: 400; font-size: 38px; fill: var(--white); }
  .variant { font-family: 'Montserrat', sans-serif; font-weight: 600; font-size: 23px; letter-spacing: 6px; fill: var(--gold); }
  .spec-text { font-family: 'Montserrat', sans-serif; font-weight: 400; font-size: 15px; fill: var(--white); }
  .estimated-sign { font-family: 'Montserrat', sans-serif; font-weight: 600; font-size: 40px; fill: var(--white); }
</style>
</head>
<body>
<svg class="dieline-canvas" viewBox="0 0 1500 2145" xmlns="http://www.w3.org/2000/svg">
  <defs>
    <clipPath id="box-shape">
      <path id="dieline" d="M125,571 L306,573 L341,694 L365,720 L367,754 L650,751 L645,727 L672,700 L705,571 L888,573 L895,726 L912,750 L919,745 L919,475 L928,472 L928,410 L948,381 L975,364 L1147,364 L1173,383 L1190,410 L1191,478 L1199,478 L1199,1584 L916,1582 L918,1607 L890,1640 L863,1754 L682,1754 L666,1594 L643,1585 L363,1583 L343,1603 L332,1758 L143,1752 L115,1632 L92,1615 L92,745 L110,733 Z"/>
    </clipPath>
    <radialGradient id="foliage-left" cx="0.5" cy="0.5" r="0.5">
      <stop offset="0" stop-color="#4a5736" stop-opacity="0.95"/>
      <stop offset="0.6" stop-color="#475433" stop-opacity="0.6"/>
      <stop offset="1" stop-color="#3b4733" stop-opacity="0"/>
    </radialGradient>
    <radialGradient id="foliage-right" cx="0.5" cy="0.5" r="0.5">
      <stop offset="0" stop-color="#56653d" stop-opacity="0.95"/>
      <stop offset="0.6" stop-color="#505e39" stop-opacity="0.6"/>
      <stop offset="1" stop-color="#3b4733" stop-opacity="0"/>
    </radialGradient>
    <radialGradient id="foliage-mid" cx="0.5" cy="0.5" r="0.5">
      <stop offset="0" stop-color="#4e5c38" stop-opacity="0.8"/>
      <stop offset="1" stop-color="#3b4733" stop-opacity="0"/>
    </radialGradient>
    <linearGradient id="foliage-flaps" x1="0" y1="0" x2="1" y2="1">
      <stop offset="0" stop-color="#4e5c38"/>
      <stop offset="0.5" stop-color="#3e4a34"/>
      <stop offset="1" stop-color="#4a5736"/>
    </linearGradient>
  </defs>

  <g clip-path="url(#box-shape)">
    <rect class="box-surface" x="0" y="0" width="1500" height="2145"/>
    <g role="img" aria-label="Hanfblätter als Hintergrundillustration">
      <ellipse cx="330" cy="1180" rx="300" ry="260" fill="url(#foliage-left)"/>
      <ellipse cx="150" cy="1290" rx="140" ry="110" fill="url(#foliage-mid)"/>
      <ellipse cx="700" cy="1260" rx="260" ry="150" fill="url(#foliage-mid)"/>
      <ellipse cx="1020" cy="1120" rx="260" ry="300" fill="url(#foliage-right)"/>
      <ellipse cx="1150" cy="1270" rx="120" ry="200" fill="url(#foliage-right)"/>
    </g>
    <rect x="92" y="1582" width="830" height="180" fill="url(#foliage-flaps)" role="img" aria-label="Hanfblätter auf den Bodenlaschen"/>
    <rect class="info-band" x="92" y="1376" width="1110" height="208"/>
  </g>
  <use href="#dieline" class="box-outline"/>

  <text class="brand-top" x="785" y="828" text-anchor="middle">XXX</text>

  <g class="badge">
    <path class="badge-arc" d="M666,955 A128,128 0 0 1 898,940"/>
    <path class="badge-arc" d="M668,1090 A128,128 0 0 0 903,1085"/>
    <circle class="badge-ring" cx="784" cy="1018" r="124"/>
    <circle class="badge-core" cx="784" cy="1018" r="102"/>
    <text class="badge-name" x="784" y="1034" text-anchor="middle">XXXX</text>
  </g>

  <text class="product-title" x="787" y="1218" text-anchor="middle">CBD ÖL</text>
  <line class="rule-line" x1="660" y1="1230" x2="906" y2="1230"/>
  <text class="variant" x="790" y="1259" text-anchor="middle">MILD</text>
  <line class="rule-line" x1="660" y1="1269" x2="906" y2="1269"/>

  <text class="spec-text" x="717" y="1542" text-anchor="middle">2000mg CBD</text>
  <text class="estimated-sign" x="878" y="1520" text-anchor="middle">℮</text>
  <text class="spec-text" x="879" y="1542" text-anchor="middle">10 ml</text>
</svg>
</body>
</html>
```